Report template for evaluation reports to be used by non designers

We are looking for a report template that meets all the requirements listed in the attached documents. letter head, logo etc have been enclosed. Its important that the colour integrity is kept, but beyond that options are welcome.
Its important that the document is extremely easy to use and that is able to be adapted to include eatables, figures, pictures, text boxes etc and keep the integrity of the template

Target Market(s)

Governments, Civil society organisations and research institutions

Font styles to use
Sans Serif

Colors
6b449b
876aae
c0c0c0
000000

Requirements
Must have
• Clean, professional, not concluded, modern, must be easy to use
Should not have
• too busy, hard to use

```html
<!DOCTYPE html>
<html lang="en">
<head>
<meta charset="utf-8">
<title>Report Template – Linden Policy Institute</title>
<link href="https://fonts.googleapis.com/css2?family=Arimo:wght@400;700&display=swap" rel="stylesheet">
<style>
  :root {
    --purple: #5c4191;
    --purple-light: #876aae;
    --grey: #c0c0c0;
    --ink: #1a1a1a;
    --paper: #f7f7f6;
    --stage: #000000;
  }
  * { box-sizing: border-box; margin: 0; padding: 0; }
  html, body { width: 905px; height: 1200px; overflow: hidden; background: var(--stage); }
  body { position: relative; font-family: "Arimo", Arial, sans-serif; color: var(--ink); }

  .page {
    position: absolute; width: 363px; height: 514px;
    background: var(--paper); overflow: hidden;
  }
  .page--cover { left: 75px; top: 64px; }
  .page--letter { left: 466px; top: 64px; }
  .page--index { left: 75px; top: 621px; }
  .page--memo { left: 466px; top: 621px; }

  .brand {
    position: absolute; font-size: 13px; font-weight: 400;
    letter-spacing: 2.4px; color: var(--ink); white-space: nowrap;
  }
  .brand__dot {
    display: inline-block; width: 7px; height: 7px; border-radius: 50%;
    background: var(--purple); margin-right: 5px; vertical-align: 1px;
  }
  .page--cover .brand, .page--letter .brand, .page--index .brand { left: 32px; top: 28px; }
  .page--memo .brand { right: 22px; top: 36px; }

  .cover-title {
    position: absolute; left: 0; right: 0; top: 180px; text-align: center;
    color: var(--purple); font-weight: 700; font-size: 34px; line-height: 42px;
  }
  .cover-author {
    position: absolute; left: 0; right: 0; top: 272px; text-align: center;
    color: var(--purple); font-weight: 700; font-size: 16px;
  }
  .cover-date {
    position: absolute; left: 0; right: 0; top: 294px; text-align: center;
    font-size: 10px;
  }
  .cover-band { position: absolute; left: 0; bottom: 0; width: 363px; height: 60px; }

  .footer { position: absolute; left: 22px; width: 320px; top: 474px; }
  .footer__contacts {
    display: flex; justify-content: space-between; align-items: center;
    font-size: 5px; white-space: nowrap; padding-bottom: 3px;
    border-bottom: 0.8px solid var(--purple-light);
  }
  .footer__item { display: flex; align-items: center; gap: 2px; }
  .footer__icon { width: 6px; height: 6px; }
  .footer__services {
    text-align: center; font-size: 5.4px; font-weight: 700;
    color: var(--purple); margin-top: 5px; word-spacing: 1px;
  }
  .footer__services span { color: var(--ink); font-weight: 400; margin: 0 3px; }

  .index-title {
    position: absolute; left: 34px; top: 80px; font-size: 14px; font-weight: 700;
    color: var(--purple); letter-spacing: 0.2px;
  }
  .index-rule { position: absolute; left: 34px; width: 296px; top: 103px; border-top: 1px solid var(--purple-light); }
  .index-table { position: absolute; left: 34px; top: 111px; width: 296px; height: 324px; }
  .index-table__col {
    position: absolute; top: 0; bottom: 0; border-left: 0.8px solid var(--grey);
  }
  .index-table__row {
    position: absolute; left: 0; width: 296px; height: 18.6px;
    font-size: 4.8px; display: flex; align-items: center;
  }
  .index-table__row--body { border-bottom: 0.8px solid var(--purple-light); }
  .cell-no { width: 32px; padding-left: 10px; }
  .cell-topic { width: 215px; padding-left: 0; }
  .cell-page { padding-left: 14px; }
  .index-table__row--head .cell-no { padding-left: 2px; }
  .index-table__row--head .cell-topic { padding-left: 2px; }
  .index-table__row--head .cell-page { padding-left: 2px; }
  .cell-topic, .cell-page { margin-left: 0; }

  .memo-name {
    position: absolute; left: 21px; top: 44px; font-size: 8px; font-weight: 700; color: var(--purple);
  }
  .memo-date { position: absolute; left: 21px; top: 56px; font-size: 3.2px; font-weight: 700; }
  .memo-rule { position: absolute; left: 21px; width: 321px; top: 67px; border-top: 0.8px solid var(--purple-light); }
  .disclaimer { position: absolute; left: 22px; top: 436px; width: 320px; font-size: 3.4px; line-height: 4.2px; color: #777; }
  .disclaimer__title { color: var(--purple); font-weight: 700; font-size: 3.8px; }
</style>
</head>
<body>

<section class="page page--cover">
  <div class="brand"><span class="brand__dot"></span>LINDEN POLICY INSTITUTE</div>
  <h1 class="cover-title">NAME<br>of the report</h1>
  <p class="cover-author">Anna Keller</p>
  <p class="cover-date">on 27th June 2018</p>
  <svg class="cover-band" viewBox="0 0 363 60" aria-hidden="true">
    <polygon points="0,0 363,60 0,60" fill="var(--purple)"/>
  </svg>
</section>

<section class="page page--letter">
  <div class="brand"><span class="brand__dot"></span>LINDEN POLICY INSTITUTE</div>
  <footer class="footer">
    <div class="footer__contacts">
      <span class="footer__item"><svg class="footer__icon" viewBox="0 0 10 10"><circle cx="5" cy="5" r="4.3" fill="none" stroke="var(--ink)" stroke-width="1"/><rect x="3" y="3.5" width="4" height="3" fill="var(--ink)"/></svg>+41780001234</span>
      <span class="footer__item"><svg class="footer__icon" viewBox="0 0 10 10"><circle cx="5" cy="5" r="4.3" fill="none" stroke="var(--ink)" stroke-width="1"/><rect x="2.8" y="3.5" width="4.4" height="3" fill="none" stroke="var(--ink)" stroke-width="0.8"/></svg>info@lindeninstitute.org</span>
      <span class="footer__item"><svg class="footer__icon" viewBox="0 0 10 10"><circle cx="5" cy="5" r="4.3" fill="none" stroke="var(--ink)" stroke-width="1"/><circle cx="5" cy="5" r="2" fill="none" stroke="var(--ink)" stroke-width="0.8"/></svg>www.lindeninstitute.org</span>
      <span class="footer__item"><svg class="footer__icon" viewBox="0 0 10 10"><circle cx="5" cy="5" r="4.3" fill="none" stroke="var(--ink)" stroke-width="1"/><path d="M3 6.5 L7 3.5" stroke="var(--ink)" stroke-width="0.8"/></svg>Registration Number: CHF-000.512.880</span>
    </div>
    <p class="footer__services">Evaluation<span>|</span>Research<span>|</span>Policy Analysis<span>|</span>Capacity Development<span>|</span>Training</p>
  </footer>
</section>

<section class="page page--index">
  <div class="brand"><span class="brand__dot"></span>LINDEN POLICY INSTITUTE</div>
  <h2 class="index-title">EXAMPLE OF INDEX</h2>
  <div class="index-rule"></div>
  <div class="index-table">
    <div class="index-table__col" style="left:32px"></div>
    <div class="index-table__col" style="left:247px"></div>
    <div class="index-table__row index-table__row--head" style="top:0"><span class="cell-no">S.No.</span><span class="cell-topic">TOPIC</span><span class="cell-page">Page No.</span></div>
    <div class="index-table__row index-table__row--body" style="top:12px"><span class="cell-no">1)</span><span class="cell-topic">LOREM IPSUM</span><span class="cell-page">1</span></div>
    <div class="index-table__row index-table__row--body" style="top:30.6px"><span class="cell-no">2)</span><span class="cell-topic">LOREM IPSUM</span><span class="cell-page">2</span></div>
    <div class="index-table__row index-table__row--body" style="top:49.2px"><span class="cell-no">3)</span><span class="cell-topic">LOREM IPSUM</span><span class="cell-page">3</span></div>
    <div class="index-table__row index-table__row--body" style="top:67.8px"><span class="cell-no">4)</span><span class="cell-topic">LOREM IPSUM</span><span class="cell-page">4</span></div>
    <div class="index-table__row index-table__row--body" style="top:86.4px"><span class="cell-no">5)</span><span class="cell-topic">LOREM IPSUM</span><span class="cell-page">5</span></div>
    <div class="index-table__row index-table__row--body" style="top:105px"><span class="cell-no">6)</span><span class="cell-topic">LOREM IPSUM</span><span class="cell-page">6</span></div>
    <div class="index-table__row index-table__row--body" style="top:123.6px"><span class="cell-no">7)</span><span class="cell-topic">LOREM IPSUM</span><span class="cell-page">7</span></div>
    <div class="index-table__row index-table__row--body" style="top:142.2px"><span class="cell-no">8)</span><span class="cell-topic">LOREM IPSUM</span><span class="cell-page">8</span></div>
    <div class="index-table__row index-table__row--body" style="top:160.8px"><span class="cell-no">9)</span><span class="cell-topic">LOREM IPSUM</span><span class="cell-page">9</span></div>
    <div class="index-table__row index-table__row--body" style="top:179.4px"><span class="cell-no">10)</span><span class="cell-topic">LOREM IPSUM</span><span class="cell-page">10</span></div>
    <div class="index-table__row index-table__row--body" style="top:198px"><span class="cell-no">11)</span><span class="cell-topic">LOREM IPSUM</span><span class="cell-page">11</span></div>
    <div class="index-table__row index-table__row--body" style="top:216.6px"><span class="cell-no">12)</span><span class="cell-topic">LOREM IPSUM</span><span class="cell-page">12</span></div>
    <div class="index-table__row index-table__row--body" style="top:235.2px"><span class="cell-no">13)</span><span class="cell-topic">LOREM IPSUM</span><span class="cell-page">13</span></div>
    <div class="index-table__row index-table__row--body" style="top:253.8px"><span class="cell-no">14)</span><span class="cell-topic">LOREM IPSUM</span><span class="cell-page">14</span></div>
  </div>
  <footer class="footer">
    <div class="footer__contacts">
      <span class="footer__item"><svg class="footer__icon" viewBox="0 0 10 10"><circle cx="5" cy="5" r="4.3" fill="none" stroke="var(--ink)" stroke-width="1"/><rect x="3" y="3.5" width="4" height="3" fill="var(--ink)"/></svg>+41780001234</span>
      <span class="footer__item"><svg class="footer__icon" viewBox="0 0 10 10"><circle cx="5" cy="5" r="4.3" fill="none" stroke="var(--ink)" stroke-width="1"/><rect x="2.8" y="3.5" width="4.4" height="3" fill="none" stroke="var(--ink)" stroke-width="0.8"/></svg>info@lindeninstitute.org</span>
      <span class="footer__item"><svg class="footer__icon" viewBox="0 0 10 10"><circle cx="5" cy="5" r="4.3" fill="none" stroke="var(--ink)" stroke-width="1"/><circle cx="5" cy="5" r="2" fill="none" stroke="var(--ink)" stroke-width="0.8"/></svg>www.lindeninstitute.org</span>
      <span class="footer__item"><svg class="footer__icon" viewBox="0 0 10 10"><circle cx="5" cy="5" r="4.3" fill="none" stroke="var(--ink)" stroke-width="1"/><path d="M3 6.5 L7 3.5" stroke="var(--ink)" stroke-width="0.8"/></svg>Registration Number: CHF-000.512.880</span>
    </div>
    <p class="footer__services">Evaluation<span>|</span>Research<span>|</span>Policy Analysis<span>|</span>Capacity Development<span>|</span>Training</p>
  </footer>
</section>

<section class="page page--memo">
  <p class="memo-name">Mara Olsen</p>
  <p class="memo-date">22nd June 2018</p>
  <div class="brand"><span class="brand__dot"></span>LINDEN POLICY INSTITUTE</div>
  <div class="memo-rule"></div>
  <div class="disclaimer">
    <p class="disclaimer__title">DISCLAIMER</p>
    <p>The views expressed in this report are those of the authors and do not necessarily reflect the position of the institute or its partners. Findings are based on data available at the time of writing and may change as new evidence emerges. The institute accepts no liability for decisions made on the basis of this material. Reproduction is permitted for non-commercial use provided the source is clearly acknowledged in full.</p>
  </div>
  <footer class="footer">
    <div class="footer__contacts">
      <span class="footer__item"><svg class="footer__icon" viewBox="0 0 10 10"><circle cx="5" cy="5" r="4.3" fill="none" stroke="var(--ink)" stroke-width="1"/><rect x="3" y="3.5" width="4" height="3" fill="var(--ink)"/></svg>+41780001234</span>
      <span class="footer__item"><svg class="footer__icon" viewBox="0 0 10 10"><circle cx="5" cy="5" r="4.3" fill="none" stroke="var(--ink)" stroke-width="1"/><rect x="2.8" y="3.5" width="4.4" height="3" fill="none" stroke="var(--ink)" stroke-width="0.8"/></svg>info@lindeninstitute.org</span>
      <span class="footer__item"><svg class="footer__icon" viewBox="0 0 10 10"><circle cx="5" cy="5" r="4.3" fill="none" stroke="var(--ink)" stroke-width="1"/><circle cx="5" cy="5" r="2" fill="none" stroke="var(--ink)" stroke-width="0.8"/></svg>www.lindeninstitute.org</span>
      <span class="footer__item"><svg class="footer__icon" viewBox="0 0 10 10"><circle cx="5" cy="5" r="4.3" fill="none" stroke="var(--ink)" stroke-width="1"/><path d="M3 6.5 L7 3.5" stroke="var(--ink)" stroke-width="0.8"/></svg>Registration Number: CHF-000.512.880</span>
    </div>
    <p class="footer__services">Evaluation<span>|</span>Research<span>|</span>Policy Analysis<span>|</span>Capacity Development<span>|</span>Training</p>
  </footer>
</section>

</body>
</html>
```